Stationery Set for new venture capital firm

We need a new set of stationery including letterhead, business cards, envelopes, with compliment slips for our new startup venture capital firm known as Halvorn.
We make alternative investments globally and hope to have a worldwide network of offices later.

The stationery should be elegant and not too fussy with the use of too many colors.

Venture Capital

```html
<!DOCTYPE html>
<html lang="en">
<head>
<meta charset="utf-8">
<title>Halvorn Stationery</title>
<link href="https://fonts.googleapis.com/css2?family=Open+Sans:wght@400;600;700&display=swap" rel="stylesheet">
<style>
  :root {
    --bg: #ececec;
    --paper: #fafafa;
    --blue: #1b8fd0;
    --ink: #4a4c4f;
    --grey: #707275;
    --faint: #e3e3e4;
    --shadow: 0 2px 6px rgba(0,0,0,.10);
  }
  * { box-sizing: border-box; margin: 0; padding: 0; }
  html, body { width: 1200px; height: 795px; overflow: hidden; background: var(--bg); }
  body { position: relative; font-family: "Open Sans", sans-serif; color: var(--ink); }

  .sheet { position: absolute; background: var(--paper); box-shadow: var(--shadow); overflow: hidden; }

  .wordmark { display: flex; align-items: center; gap: 6px; font-weight: 700; color: var(--grey); letter-spacing: .5px; }
  .wordmark .dot { display: inline-block; border-radius: 50%; background: var(--blue); }

  .faint-mark { position: absolute; border-radius: 50%; background: var(--faint); }

  /* Letterhead */
  .letterhead { left: 380px; top: 40px; width: 340px; height: 480px; padding: 34px 32px; }
  .letterhead .wordmark { font-size: 17px; }
  .letterhead .wordmark .dot { width: 14px; height: 14px; }
  .letter-body { margin-top: 30px; width: 230px; font-size: 6.2px; line-height: 1.6; color: var(--grey); position: relative; z-index: 1; }
  .letter-body .salutation { font-weight: 700; color: var(--ink); margin-bottom: 8px; }
  .letter-body p { margin-bottom: 8px; }
  .signature { width: 70px; height: 20px; margin-top: 20px; background: linear-gradient(90deg, #d9d9da, #ececec); }
  .sign-role { font-size: 6.5px; font-weight: 700; color: var(--ink); margin-top: 3px; }
  .letterhead .faint-mark { width: 150px; height: 150px; right: -20px; top: 180px; }
  .footer { position: absolute; left: 32px; right: 32px; bottom: 26px; display: flex; justify-content: space-between; align-items: flex-end; font-size: 5.6px; line-height: 1.6; color: var(--grey); }
  .footer .phones { border-left: 3px solid var(--blue); padding-left: 6px; }
  .footer .web { color: var(--blue); }

  /* Compliment slip */
  .slip { left: 760px; top: 420px; width: 410px; height: 200px; padding: 22px 26px; }
  .slip .wordmark { font-size: 15px; }
  .slip .wordmark .dot { width: 12px; height: 12px; }
  .slip .faint-mark { width: 110px; height: 110px; right: 50px; top: 10px; }
  .slip .greeting { position: absolute; right: 26px; top: 52px; font-size: 15px; color: var(--blue); }
  .slip .footer { left: 26px; right: 26px; bottom: 20px; }

  /* Business cards */
  .card { width: 210px; height: 120px; }
  .card-back { left: 40px; top: 70px; display: flex; flex-direction: column; align-items: center; justify-content: center; }
  .card-back .wordmark { font-size: 15px; margin-top: -14px; }
  .card-back .wordmark .dot { width: 12px; height: 12px; }
  .card-back .band { position: absolute; left: 0; right: 0; bottom: 22px; height: 12px; background: var(--blue); color: #fff; font-size: 5.5px; text-align: center; line-height: 12px; }
  .card-front { left: 40px; top: 215px; padding: 16px 16px; font-size: 5.6px; line-height: 1.6; color: var(--grey); }
  .card-front .dot-mark { position: absolute; right: 16px; top: 16px; width: 18px; height: 18px; border-radius: 50%; background: var(--blue); }
  .card-front .web { position: absolute; right: 16px; top: 42px; color: var(--blue); }
  .card-front .name { font-size: 8px; font-weight: 600; color: var(--blue); margin-top: 26px; }
  .card-front .role { font-size: 5.5px; text-transform: uppercase; letter-spacing: .5px; margin-bottom: 6px; }

  /* Notebook */
  .notebook { left: 70px; top: 390px; width: 270px; height: 360px; display: flex; align-items: center; justify-content: center; }
  .notebook .wordmark { font-size: 26px; }
  .notebook .wordmark .dot { width: 22px; height: 22px; }
  .spiral { position: absolute; left: 6px; top: 12px; bottom: 12px; width: 8px;
    background: repeating-linear-gradient(180deg, #3a3a3c 0 3px, transparent 3px 11px); }
</style>
</head>
<body>

  <section class="sheet card card-back">
    <div class="wordmark"><span class="dot"></span>Halvorn</div>
    <div class="band">www.halvorn-capital.co</div>
  </section>

  <section class="sheet card card-front">
    <span class="dot-mark"></span>
    <span class="web">www.halvorn-capital.co</span>
    <div class="name">Ines Marlowe</div>
    <div class="role">Manager</div>
    <div>t. +44 20 7946 0182<br>f. +44 20 7946 0195<br>e. hello@halvorn-capital.co</div>
    <div>12th Floor, Meridian House Offices<br>8 Quayside Lane, Leith, Edinburgh</div>
  </section>

  <section class="sheet notebook">
    <span class="spiral"></span>
    <div class="wordmark"><span class="dot"></span>Halvorn</div>
  </section>

  <section class="sheet letterhead">
    <div class="wordmark"><span class="dot"></span>Halvorn</div>
    <span class="faint-mark"></span>
    <div class="letter-body">
      <div class="salutation">Dear Partner,</div>
      <p>Thank you for meeting with our team last week. We were pleased to learn more about your plans and the market you are building for, and we look forward to continuing the conversation in the months ahead.</p>
      <p>As discussed, Halvorn invests in early stage companies across several regions. Our partners bring long experience in finance, operations and growth, and we aim to support founders well beyond the first round.</p>
      <p>Enclosed you will find a short summary of our proposed terms, along with the next steps we suggest for review.</p>
      <p>Please do not hesitate to contact me should you have any questions. We remain at your disposal.</p>
      <div class="signature" role="img" aria-label="Handwritten signature"></div>
      <div class="sign-role">Company Director</div>
    </div>
    <div class="footer">
      <div class="phones">t. +44 20 7946 0182<br>f. +44 20 7946 0195</div>
      <div>12th Floor, Meridian House Offices<br>8 Quayside Lane, Leith, Edinburgh</div>
      <div>hello@halvorn-capital.co<br><span class="web">www.halvorn-capital.co</span></div>
    </div>
  </section>

  <section class="sheet slip">
    <div class="wordmark"><span class="dot"></span>Halvorn</div>
    <span class="faint-mark"></span>
    <div class="greeting">With compliments</div>
    <div class="footer">
      <div class="phones">t. +44 20 7946 0182<br>f. +44 20 7946 0195</div>
      <div>12th Floor, Meridian House Offices<br>8 Quayside Lane, Leith, Edinburgh</div>
      <div>hello@halvorn-capital.co<br><span class="web">www.halvorn-capital.co</span></div>
    </div>
  </section>

</body>
</html>
```